Security and Technology Website - Bold and Confident, Something Unexpected

Silver Heron Systems is launching its first website and we need a great design to bring our brand to life and generate DTC and B2B leads.

We have a good logo, but I am struggling with the creative vision to bring it all together. While our industry is Alarm Systems and Technology, we want to create a site that is more friendly and less 'typical' than your standard IT sites.

It Must:
1. Appeal to both men and women. The logo is a bit masculine, so the colors and icons must soften this.
2. Feel modern - we need to convey that we we use the latest technology.
3. Feel a bit high-end. We are not a budget solution.
4. Have a distinct iconography and photo treatment.
5. Feel layered - not just a series of stacked horizontal modules.

It Should Not:
1. Feel like your typical IT website.

Here are resources to get you started!
• Staging Site:
https://silver-heron-systems.examplestore.test/
Password: Pippa

•Brand Guide: https://www.sketchboardly.test/design/QWRtLmPOx4K/vBnm8Kq2-ZXyTrLp7hd-QE/edit?utm_content=QWRtLmPOx4K&utm_campaign=designshare&utm_medium=link2&utm_source=sharebutton

• Logo and Fonts and Photos: :https://files.cloudvaultia.test/folders/7KpWmQ3xNrT8yLbZ2vHcJ5dFg9sAeUoPi?usp=sharing

• Design Inspiration (don't feel limited by this): https://www.sketchboardly.test/design/HJkPqRvBn2s/m7TyUiOp4LkJhGfDsA2-ZX/edit?utm_content=HJkPqRvBn2s&utm_campaign=designshare&utm_medium=link2&utm_source=sharebutton

______________

The winner will be asked to provide design files and finished PNGs of the overall design file, backgrounds, photo treatments/frames, and icons.

The winner will likely be engaged for a phase 2 to build out a product page.

Industry/Entity Type

Alarm Systems, Home Theatres, and Commercial IT Networking

Number of Pages Required

1 page

Font styles to use
Sans Serif

Colors
0054AA
0677BA
7BADD7
CADEEF
E8F1F8
0094D4
00A9DD
6FCCEA
C7EBF8
E9F6FB
EB3D1F
EC4F4E
F09395
F8D3D4
FCEDEE

Requirements
Must have
• 1. Appeal to both men and women. The logo is a bit masculine, so the colors and icons must soften this. 2. Feel modern - we need to convey that we we use the latest technology. 3. Feel a bit high-end. We are not a budget solution. 4. Have a distinct iconography and photo treatment. 5. Feel layered - not just a series of stacked horizontal modules.
Should not have
• 1. Should not feel like just another IT website.

```html
<!DOCTYPE html>
<html lang="en">
<head>
<meta charset="utf-8">
<title>Silver Heron Systems — Safer. Smarter. Faster.</title>
<link rel="stylesheet" href="https://fonts.googleapis.com/css2?family=Russo+One&family=Poppins:wght@400;500;600;700&display=swap">
<style>
:root{
  --blue-deep:#0054AA;
  --blue:#0677BA;
  --blue-soft:#7BADD7;
  --blue-pale:#CADEEF;
  --blue-mist:#E8F1F8;
  --sky:#0094D4;
  --cyan:#00A9DD;
  --cyan-soft:#6FCCEA;
  --cyan-mist:#E9F6FB;
  --red:#EB3D1F;
  --red-soft:#EC4F4E;
  --red-brand:#e3132b;
  --navy:#1b3d8f;
  --ink:#1c1c24;
  --grey:#6b6b75;
  --white:#ffffff;
  --display:"Russo One", sans-serif;
  --body:"Poppins", sans-serif;
}
*{box-sizing:border-box;margin:0;padding:0}
html,body{width:1200px;height:3831px;overflow:hidden;background:var(--white)}
body{font-family:var(--body);color:var(--ink)}
.page{position:relative;width:1200px;height:3831px;overflow:hidden}
.abs{position:absolute}
.center{left:0;right:0;text-align:center}

/* top bar */
.topbar{top:0;left:0;width:1200px;height:36px;background:linear-gradient(90deg,#d5102a 0%,#c01a3a 60%,#1d4aa5 82%,#0d5ec0 100%)}
.topbar a{position:absolute;top:9px;font-family:var(--display);font-size:15px;letter-spacing:1.5px;color:var(--white);text-decoration:none}
.social-dot{position:absolute;top:9px;width:17px;height:17px;border:2px solid var(--white);border-radius:3px}

/* header */
.header{top:36px;left:0;width:1200px;height:111px;background:var(--white);box-shadow:0 2px 6px rgba(0,0,0,.06)}
.brand{position:absolute;display:flex;align-items:center;gap:8px}
.brand-mark{width:14px;height:14px;background:var(--red-brand)}
.brand-name{font-family:var(--display);font-size:15px;color:var(--blue-deep);line-height:1.05;width:92px}
.nav a{position:absolute;top:44px;font-family:var(--display);font-size:13px;color:var(--blue-deep);text-decoration:none;letter-spacing:.5px}
.nav a::after{content:"\2304";font-size:11px;margin-left:6px;position:relative;top:-3px}
.quote-btn{position:absolute;top:34px;left:992px;width:150px;height:38px;border-radius:20px;background:linear-gradient(90deg,#1b3d8f,#d5102a);color:var(--white);font-family:var(--display);font-size:13px;letter-spacing:1px;display:flex;align-items:center;justify-content:center}

/* hero */
.hero{top:147px;left:0;width:1200px;height:494px;overflow:hidden;
  background:
    radial-gradient(ellipse 420px 300px at 1180px 0,rgba(225,20,45,.9),transparent 70%),
    radial-gradient(ellipse 520px 380px at 0 420px,rgba(220,25,60,.95),transparent 70%),
    linear-gradient(180deg,#23308a 0%,#1548b0 55%,#0a5fd0 100%)}
.hero .eyebrow{top:34px;font-size:13px;font-weight:500;color:var(--white);letter-spacing:.5px}
.hero .word{font-family:var(--display);font-size:78px;line-height:90px;letter-spacing:4px}
.hero .safer{top:62px;color:#ff1a2e}
.hero .smarter{top:154px;color:var(--white)}
.hero .faster{top:246px;color:#1a9cf2}
.hero .audience{top:354px;font-size:25px;color:var(--white);letter-spacing:1px}
.hero svg{position:absolute;left:0;top:0}

/* soft backdrop behind tiles */
.hex-backdrop{top:560px;left:0;width:1200px;height:649px;
  background:
    radial-gradient(ellipse 260px 220px at 120px 180px,rgba(202,222,239,.55),transparent 70%),
    radial-gradient(ellipse 300px 260px at 1080px 360px,rgba(199,235,248,.6),transparent 70%),
    radial-gradient(ellipse 240px 200px at 980px 120px,rgba(202,222,239,.45),transparent 70%),
    linear-gradient(180deg,var(--cyan-mist) 0%,#ffffff 100%)}

/* service tiles */
.tile{position:absolute;top:699px;width:251px;height:242px;border-radius:12px;overflow:hidden;box-shadow:0 10px 26px rgba(20,40,90,.22)}
.tile .photo{position:absolute;inset:0}
.tile .label{position:absolute;left:18px;bottom:16px;color:var(--white)}
.tile h3{font-family:var(--display);font-size:14px;letter-spacing:1px;margin-bottom:6px}
.tile li{font-size:12px;list-style:none;line-height:19px}
.tile li::before{content:"\2022";margin-right:6px}

/* connect heading */
.section-title{font-family:var(--display);font-size:38px;letter-spacing:1px;color:var(--blue-deep)}
.section-title .red{color:var(--red-brand)}
.lead{font-size:17px;color:#333}

/* monitoring band */
.monitor{top:1209px;left:0;width:1200px;height:467px;background:linear-gradient(160deg,#0a5cc0 0%,#0a7ad8 45%,#0d95ef 100%);overflow:hidden}
.monitor-texture{top:0;left:0;width:1200px;height:467px;background:radial-gradient(ellipse 500px 260px at 200px 120px,rgba(255,255,255,.07),transparent 70%),radial-gradient(ellipse 500px 260px at 1000px 360px,rgba(255,255,255,.07),transparent 70%)}
.feature{position:absolute;top:1111px;width:158px;height:213px;background:var(--white);border-radius:8px;box-shadow:3px 4px 0 var(--cyan-soft),0 8px 18px rgba(0,40,100,.18);text-align:center;padding:12px 10px 0}
.feature svg{display:block;margin:0 auto 4px}
.feature h4{font-family:var(--display);font-size:16px;line-height:19px;color:var(--blue-deep);letter-spacing:.5px;margin-bottom:4px}
.feature p{font-size:9.5px;line-height:12px;color:var(--grey)}
.monitor h2{font-family:var(--display);color:var(--white);font-size:32px;line-height:42px;letter-spacing:2px}
.monitor p{font-size:13.5px;color:var(--white);line-height:20px}
.pill-btn{position:absolute;left:547px;width:122px;height:37px;border-radius:10px;background:#0b4aa6;color:var(--white);font-size:11px;font-weight:500;display:flex;align-items:center;justify-content:center}

/* steps */
.tab{top:1596px;left:168px;width:880px;height:120px;background:var(--white);border-radius:16px 16px 0 0}
.tab h2{font-family:var(--display);font-size:31px;line-height:40px;color:var(--navy);letter-spacing:2px}
.step{position:absolute;top:1735px;width:260px;text-align:center}
.step .num{display:flex;justify-content:center;align-items:center;gap:4px;height:90px}
.step .num span{font-family:var(--display);font-size:56px;letter-spacing:2px}
.step h5{font-family:var(--display);font-size:18px;line-height:24px;letter-spacing:1px;color:var(--ink);margin-top:22px}
.step p{font-size:10px;color:var(--grey);line-height:13px;margin-top:6px}
.step a{display:inline-block;margin-top:12px;font-size:10px;font-weight:700;color:var(--navy);text-decoration:underline}

/* reviews */
.reviews{top:1997px;left:0;width:1200px;height:266px;background:linear-gradient(110deg,#e9eaec 0%,#f4f4f6 40%,#e6e7ea 100%)}
.stars{color:var(--navy);font-size:20px;letter-spacing:2px}
.quote{font-size:15.5px;line-height:19.5px;color:var(--navy);width:510px}
.reviewer{font-size:9px;color:var(--sky)}
.arrow{position:absolute;color:var(--blue-deep);font-size:30px;font-weight:300}

/* founder */
.founder-heading{font-family:var(--display);font-size:12.5px;line-height:19px;color:var(--navy);letter-spacing:.4px;width:440px}
.founder-copy p{font-size:11px;line-height:13px;color:var(--blue-deep);font-weight:500;width:420px;margin-bottom:10px}
.btn-red{position:absolute;height:33px;border-radius:4px;background:var(--red-brand);color:var(--white);font-size:10px;font-weight:600;display:flex;align-items:center;justify-content:center;box-shadow:0 0 0 3px #fff,0 0 0 4px var(--red-brand)}
.btn-outline{position:absolute;height:33px;border-radius:4px;border:1.5px solid var(--red-brand);color:var(--red-brand);font-size:10px;font-weight:600;display:flex;align-items:center;justify-content:center}

/* partners */
.partners{top:2677px;left:0;width:1200px;height:208px;background:#eeeff1}
.partner{position:absolute;top:2781px;height:50px;border-radius:6px;background:#cfd2d8}

/* quote form */
.form-title{font-family:var(--display);font-size:29px;letter-spacing:2px;color:var(--ink)}
.field-label{position:absolute;font-size:12px;font-weight:600;color:#333}
.field{position:absolute;background:#f1f1f3;border-radius:3px}
.submit{position:absolute;left:572px;top:3304px;width:88px;height:33px;background:var(--red-brand);color:var(--white);font-size:15px;font-weight:600;border-radius:3px;display:flex;align-items:center;justify-content:center}

/* footer */
.footer{top:3387px;left:0;width:1200px;height:444px;background:linear-gradient(170deg,#563f74 0%,#3a4688 45%,#1c4fa6 100%)}
.footer-glow{left:0;bottom:0;width:1200px;height:130px;background:linear-gradient(180deg,transparent,rgba(0,148,212,.22))}
.footer h2{font-family:var(--display);font-size:26px;letter-spacing:2px;color:var(--white)}
.footer .sub{font-size:11px;color:var(--white);font-weight:500}
.news-input{position:absolute;left:357px;top:3487px;width:412px;height:34px;background:var(--white);border-radius:4px;font-size:10px;color:#999;padding:10px 12px}
.news-btn{position:absolute;left:782px;top:3487px;width:64px;height:34px;background:var(--red-brand);color:var(--white);font-size:10px;font-weight:700;border-radius:3px;display:flex;align-items:center;justify-content:center}
.foot-col{position:absolute;top:3571px;color:var(--white)}
.foot-col h6{font-family:var(--display);font-size:14px;letter-spacing:1px;color:#7fc4ff;margin-bottom:8px}
.foot-col li{list-style:none;font-size:9.5px;line-height:18px;color:#d7dcf0}
.foot-col .strong{color:var(--white);font-weight:600;text-decoration:underline}
.legal{font-size:11px;font-weight:700;color:var(--white)}
</style>
</head>
<body>
<div class="page">

  <!-- soft backdrop behind tiles and cards -->
  <div class="abs hex-backdrop" role="img" aria-label="Faint pale blue hexagon network pattern"></div>

  <!-- utility bar -->
  <div class="abs topbar">
    <a href="#" style="left:230px">ABOUT</a>
    <a href="#" style="left:380px">CONSULTING</a>
    <a href="#" style="left:567px">CONTACT</a>
    <span class="social-dot" style="left:1022px"></span>
    <span class="social-dot" style="left:1066px"></span>
  </div>

  <!-- header -->
  <header class="abs header">
    <div class="brand" style="left:24px;top:36px">
      <span class="brand-mark"></span>
      <span class="brand-name">SILVER HERON SYSTEMS</span>
    </div>
    <nav class="nav">
      <a href="#" style="left:230px">ELECTRONIC SECURITY</a>
      <a href="#" style="left:425px">AUDIO + VIDEO</a>
      <a href="#" style="left:567px">NETWORKING + COMMUNICATION</a>
      <a href="#" style="left:833px">CABLING</a>
    </nav>
    <svg class="abs" style="left:945px;top:42px" width="20" height="20" viewBox="0 0 20 20"><circle cx="8" cy="8" r="6" fill="none" stroke="#0054AA" stroke-width="1.6"/><line x1="12.5" y1="12.5" x2="18" y2="18" stroke="#0054AA" stroke-width="1.6"/></svg>
    <div class="quote-btn">REQUEST A QUOTE</div>
  </header>

  <!-- hero -->
  <section class="abs hero">
    <svg width="1200" height="494" viewBox="0 0 1200 494" aria-hidden="true">
      <path d="M0,330 C220,400 420,470 640,470 C860,470 1050,400 1200,340" fill="none" stroke="rgba(255,80,110,.55)" stroke-width="28"/>
      <path d="M0,400 C300,495 600,500 800,456 C1000,412 1100,392 1200,390 L1200,494 L0,494 Z" fill="#E9F6FB"/>
    </svg>
    <p class="abs center eyebrow">PROUDLY SERVING MIDDLE TENNESSEE</p>
    <p class="abs center word safer">SAFER.</p>
    <p class="abs center word smarter">SMARTER.</p>
    <p class="abs center word faster">FASTER.</p>
    <p class="abs center audience">HOMES + BUSINESSES</p>
  </section>

  <!-- service tiles -->
  <article class="tile" style="left:159px">
    <div class="photo" role="img" aria-label="Photo of a woman setting a wall-mounted home alarm keypad" style="background:linear-gradient(135deg,#8a7766,#c9b8a8 55%,#6a6f8a)"></div>
    <div class="photo" style="background:linear-gradient(0deg,rgba(10,20,60,.6),transparent 60%)"></div>
    <div class="label"><h3>AFFORDABLE SECURITY</h3><ul><li>For Homes</li><li>For Businesses</li></ul></div>
  </article>
  <article class="tile" style="left:476px;box-shadow:0 10px 28px rgba(230,30,40,.4)">
    <div class="photo" role="img" aria-label="Photo of a home theatre room with a large screen" style="background:linear-gradient(135deg,#7a2a20,#d65a3a 50%,#3a2228)"></div>
    <div class="photo" style="background:linear-gradient(0deg,rgba(60,10,10,.55),transparent 60%)"></div>
    <div class="label"><h3>ENVIABLE ENTERTAINMENT</h3><ul><li>Home Theatres</li><li>Smart Homes</li><li>Whole Home A/V</li></ul></div>
  </article>
  <article class="tile" style="left:793px">
    <div class="photo" role="img" aria-label="Photo of colleagues on a video conference call" style="background:linear-gradient(135deg,#3a5878,#8aa4b8 50%,#2a3448)"></div>
    <div class="photo" style="background:linear-gradient(0deg,rgba(10,25,60,.6),transparent 60%)"></div>
    <div class="label"><h3>CONNECTED BUSINESSES</h3><ul><li>Conference Systems</li><li>Phones</li><li>Networking</li><li>WiFi</li></ul></div>
  </article>

  <!-- connect heading -->
  <h2 class="abs center section-title" style="top:1018px"><span class="red">CONNECT + PROTECT</span> YOUR WORLD</h2>
  <p class="abs center lead" style="top:1068px">Lorem ipsum dolor sit amet, consectetuer adipiscing elit, sed diam</p>

  <!-- monitoring band -->
  <section class="abs monitor">
    <div class="abs monitor-texture" role="img" aria-label="Faint geometric line texture"></div>
    <h2 class="abs center" style="top:152px">24/7<br>MONITORING</h2>
    <p class="abs center" style="top:252px">LOREM IPSUM DOLOR SIT AMET, CONSECTETUER ADIPISCING ELIT, SED DIAM NONUMMY NIBH EUISMOD TINCI-<br>DUNT UT LAOREET DOLORE MAGNA ALIQUAM ERAT VOLUTPAT. UT WISI ENIM</p>
    <div class="pill-btn" style="top:312px">BUTTON&nbsp;&nbsp;›</div>
  </section>

  <!-- feature cards -->
  <div class="feature" style="left:164px">
    <svg width="44" height="40" viewBox="0 0 44 40"><g fill="none" stroke="#0094D4" stroke-width="2" stroke-linecap="round"><path d="M8,6 a18,18 0 0 1 26,0"/><path d="M13,11 a11,11 0 0 1 16,0"/><circle cx="21" cy="22" r="4"/><path d="M36,26 a14,14 0 0 1 -6,10"/></g></svg>
    <h4>ENTRY &amp;<br>MOTION<br>SENSORS</h4>
    <p>Lorem ipsum dolor sit amet, consectetuer adipiscing elit, sed diam nonummy nibh euismod tincidunt ut laoreet dolore</p>
  </div>
  <div class="feature" style="left:346px">
    <svg width="44" height="56" viewBox="0 0 44 56"><g fill="none" stroke="#0094D4" stroke-width="2" stroke-linecap="round"><rect x="13" y="10" width="18" height="34" rx="4"/><circle cx="22" cy="20" r="4"/><line x1="17" y1="36" x2="27" y2="36"/><path d="M7,18 a12,12 0 0 0 0,18"/><path d="M37,18 a12,12 0 0 1 0,18"/></g></svg>
    <h4>VIDEO<br>MONITORING</h4>
    <p>Lorem ipsum dolor sit amet, consectetuer adipiscing elit, sed diam nonummy nibh euismod tincidunt ut laoreet dolore</p>
  </div>
  <div class="feature" style="left:529px">
    <svg width="56" height="56" viewBox="0 0 56 56"><g fill="none" stroke="#0094D4" stroke-width="2" stroke-linejoin="round"><path d="M14,16 L50,26 L47,34 L12,24 Z"/><line x1="22" y1="27" x2="20" y2="38"/><line x1="8" y1="32" x2="8" y2="44"/><line x1="8" y1="38" x2="20" y2="38"/></g></svg>
    <h4>SECURITY<br>CAMERAS</h4>
    <p>Lorem ipsum dolor sit amet, consectetuer adipiscing elit, sed diam nonummy nibh euismod tincidunt ut laoreet dolore</p>
  </div>
  <div class="feature" style="left:712px">
    <svg width="56" height="56" viewBox="0 0 56 56"><g fill="none" stroke="#0094D4" stroke-width="2"><circle cx="28" cy="28" r="22"/><ellipse cx="28" cy="34" rx="7" ry="6"/><circle cx="20" cy="24" r="3"/><circle cx="25" cy="19" r="3"/><circle cx="31" cy="19" r="3"/><circle cx="36" cy="24" r="3"/></g></svg>
    <h4>PET-<br>FRIENDLY</h4>
    <p>Lorem ipsum dolor sit amet, consectetuer adipiscing elit, sed diam nonummy nibh euismod tincidunt ut laoreet dolore</p>
  </div>
  <div class="feature" style="left:894px">
    <svg width="44" height="40" viewBox="0 0 44 40"><path d="M22,2 C26,12 34,16 32,27 C30,36 14,36 12,27 C11,21 15,17 17,13 C18,19 21,20 22,18 C24,13 21,8 22,2 Z" fill="#0094D4"/></svg>
    <h4>FIRE &amp;<br>CARBON<br>MONOXIDE</h4>
    <p>Lorem ipsum dolor sit amet, consectetuer adipiscing elit, sed diam nonummy nibh euismod tincidunt ut laoreet dolore</p>
  </div>

  <!-- 1-2-3 -->
  <div class="abs tab">
    <h2 class="abs center" style="top:35px">A SAFER HOME OR BUSINESS IS<br>AS EASY AS <span style="color:var(--red-brand)">1-2-3</span></h2>
  </div>
  <svg class="abs" style="left:548px;top:1703px" width="114" height="10" viewBox="0 0 114 10" aria-hidden="true"><line x1="4" y1="5" x2="110" y2="5" stroke="#7BADD7" stroke-width="1.5"/><circle cx="4" cy="5" r="3" fill="#fff" stroke="#7BADD7"/><circle cx="110" cy="5" r="3" fill="#fff" stroke="#7BADD7"/></svg>

  <div class="step" style="left:203px">
    <div class="num"><span style="color:var(--navy)">01</span><svg width="80" height="80" viewBox="0 0 80 80"><path d="M4,10 L32,10 L60,40 L32,70 L4,70 L32,40 Z" fill="#0677BA"/><path d="M36,16 L50,16 L74,40 L50,64 L36,64 L58,40 Z" fill="#6FCCEA"/></svg></div>
    <h5>BUILD AN<br><span style="color:var(--sky)">INSTANT QUOTE</span></h5>
    <p>Lorem ipsum dolor sit amet,<br>consectetuer adipiscing elit</p>
    <a href="#">Get Started</a>
  </div>
  <div class="step" style="left:478px">
    <div class="num"><span style="color:var(--red-brand)">02</span><svg width="80" height="80" viewBox="0 0 80 80"><path d="M4,10 L32,10 L60,40 L32,70 L4,70 L32,40 Z" fill="#e3132b"/><path d="M36,16 L50,16 L74,40 L50,64 L36,64 L58,40 Z" fill="#F09395"/></svg></div>
    <h5><span style="color:var(--red-brand)">SCHUDULE</span><br>INSTALLATION</h5>
    <p>Lorem ipsum dolor sit amet,<br>consectetuer adipiscing elit</p>
  </div>
  <div class="step" style="left:764px">
    <div class="num"><span style="color:var(--sky)">03</span><svg width="80" height="80" viewBox="0 0 80 80"><path d="M4,10 L32,10 L60,40 L32,70 L4,70 L32,40 Z" fill="#00A9DD"/><path d="M36,16 L50,16 L74,40 L50,64 L36,64 L58,40 Z" fill="#C7EBF8"/></svg></div>
    <h5>STAY SECURE<br><span style="color:var(--cyan-soft)">24/7</span></h5>
    <p>Lorem ipsum dolor sit amet,<br>consectetuer adipiscing elit</p>
  </div>

  <!-- reviews -->
  <section class="abs reviews">
    <span class="arrow" style="left:136px;top:108px">‹</span>
    <span class="arrow" style="left:1036px;top:108px">›</span>
    <p class="abs stars" style="left:167px;top:50px">★★★★★</p>
    <p class="abs quote" style="left:167px;top:82px">Fantastic sevice!! Used Brightwatch and Homelume in the past, and their custome sevice does not compare to Silver Heron! Installa-tion and set up went smoothly!!! It's so convenient to use the apps remotely for the cameras, and arming or unarm-ing the alarm. I'd rate them more than 5 stars it I was able to!</p>
    <p class="abs reviewer" style="left:167px;top:218px">- Marla T., Cedar Hollow, TN</p>
    <div class="abs" style="left:806px;top:31px;width:208px;height:208px;border-radius:50%;background:#fff;border:3px solid var(--red-brand)"></div>
    <div class="abs" style="left:860px;top:70px;width:100px;height:100px;border-radius:50%;background:#dfe3ea"></div>
  </section>

  <!-- founder -->
  <div class="abs" style="left:231px;top:2302px;width:282px;height:282px;border-radius:50%;border:2px solid var(--red-brand)"></div>
  <div class="abs" role="img" aria-label="Portrait photo of the company founder" style="left:242px;top:2313px;width:260px;height:260px;border-radius:50%;background:radial-gradient(circle at 50% 40%,#6a6a70,#2a2a30)"></div>
  <div class="abs" style="left:399px;top:2512px;width:130px;height:130px;border-radius:50%;background:#fff;border:3px solid var(--red-brand);display:flex;align-items:center;justify-content:center;flex-direction:column;gap:4px">
    <span style="width:12px;height:12px;background:var(--red-brand)"></span>
    <span style="font-family:var(--display);font-size:12px;color:var(--blue-deep);text-align:center;line-height:1.1">SILVER HERON<br>SYSTEMS</span>
  </div>
  <h3 class="abs founder-heading" style="left:584px;top:2302px">I FOUNDED SILVER HERON SYSTEMS TO BRING TOGETHER<br>TECHNOLOGY AND HONEST, RELIABLE SERVICE.</h3>
  <div class="abs founder-copy" style="left:584px;top:2358px">
    <p>I'm proud to call Tennessee home and even prouder to help keep its home and businesses secure.</p>
    <p>Whether it s protecting or elevating your space, my goal is to make technology work for you.</p>
    <p>Think of us as your friendly neighborhood tech expert here to safeguard what matters most.</p>
  </div>
  <div class="abs" role="img" aria-label="Founder's handwritten signature" style="left:588px;top:2508px;width:120px;height:52px;background:linear-gradient(90deg,rgba(0,84,170,.12),rgba(0,84,170,.04));border-radius:4px"></div>
  <div class="abs" style="left:584px;top:2595px;width:417px;height:1px;background:#bbb"></div>
  <div class="btn-red" style="left:587px;top:2615px;width:162px">TELL US HOW WE CAN HELP</div>
  <div class="btn-outline" style="left:764px;top:2615px;width:89px">ABOUT US</div>

  <!-- partners -->
  <section class="abs partners">
    <h2 class="abs center section-title" style="top:22px;font-size:29px;letter-spacing:2px">SERVICE PARTNERS</h2>
    <svg class="abs" style="left:578px;top:66px" width="44" height="10" viewBox="0 0 44 10" aria-hidden="true"><line x1="4" y1="5" x2="40" y2="5" stroke="#e3132b" stroke-width="1.5"/><circle cx="4" cy="5" r="3" fill="#fff" stroke="#e3132b"/><circle cx="40" cy="5" r="3" fill="#fff" stroke="#e3132b"/></svg>
    <span class="arrow" style="left:136px;top:108px">‹</span>
    <span class="arrow" style="left:1066px;top:108px">›</span>
  </section>
  <div class="partner" style="left:164px;width:110px"></div>
  <div class="partner" style="left:315px;width:165px"></div>
  <div class="partner" style="left:525px;width:165px"></div>
  <div class="partner" style="left:722px;width:196px"></div>
  <div class="partner" style="left:940px;width:114px"></div>

  <!-- request a quote -->
  <svg class="abs" style="left:0;top:2885px" width="560" height="502" viewBox="0 0 560 502" aria-hidden="true">
    <path d="M8,100 L500,40 L480,120 L8,150 Z" fill="#0677BA"/>
    <path d="M0,300 L90,270 L90,360 L0,400 Z" fill="#0094D4"/>
    <path d="M470,62 L536,52 L534,62 L470,72 Z" fill="#e3132b"/>
    <path d="M460,90 L530,80" stroke="#e3132b" stroke-width="6"/>
  </svg>
  <div class="abs" role="img" aria-label="Photo of a woman in a green top on a video call with her team" style="left:42px;top:2952px;width:441px;height:394px;background:linear-gradient(135deg,#cfd4d6,#7d8a82 45%,#2f4a36 80%,#1f2a2a)"></div>
  <h2 class="abs form-title" style="left:572px;top:2948px">REQUEST A QUOTE</h2>
  <span class="field-label" style="left:572px;top:3006px">Name</span>
  <span class="field-label" style="left:819px;top:3006px">Email*</span>
  <div class="field" style="left:572px;top:3026px;width:231px;height:31px"></div>
  <div class="field" style="left:819px;top:3026px;width:232px;height:31px"></div>
  <span class="field-label" style="left:572px;top:3073px">Phone</span>
  <div class="field" style="left:572px;top:3096px;width:479px;height:31px"></div>
  <span class="field-label" style="left:572px;top:3144px">Message</span>
  <div class="field" style="left:572px;top:3164px;width:479px;height:122px"></div>
  <div class="submit">Submit</div>

  <!-- footer -->
  <footer class="abs footer">
    <div class="abs footer-glow" role="img" aria-label="Soft blue circuit-board glow along the footer base"></div>
    <h2 class="abs center" style="top:20px">SUBSCRIBE TO OUR NEWSLETTER</h2>
    <p class="abs center sub" style="top:66px">Security Tips, Special Offers and More!</p>
  </footer>
  <div class="news-input">Your email</div>
  <div class="news-btn">SIGN UP</div>

  <div class="brand" style="left:141px;top:3576px">
    <span class="brand-mark"></span>
    <span class="brand-name" style="color:var(--white)">SILVER HERON SYSTEMS</span>
  </div>
  <p class="abs" style="left:141px;top:3664px;font-size:9.5px;line-height:16px;color:#d7dcf0">PROUDLY SERVING<br>MIDDLE TENNESSEE</p>
  <span class="social-dot" style="left:158px;top:3712px"></span>
  <span class="social-dot" style="left:186px;top:3712px"></span>

  <div class="foot-col" style="left:387px">
    <h6>CONTACT</h6>
    <ul><li style="line-height:12px">412 Beacon Ridge Rd. Suite 2-108<br>Millbrook, TN 37000</li><li class="strong" style="margin-top:6px">615.555.0142</li><li class="strong">Request a Quote</li></ul>
  </div>
  <div class="foot-col" style="left:659px">
    <h6>RESIDENTIAL</h6>
    <ul><li>Home Security</li><li>Smart Homes</li><li>Home Theatre +A/V</li><li>WiFi</li><li>Cabling</li></ul>
  </div>
  <div class="foot-col" style="left:929px">
    <h6>COMMERCIAL</h6>
    <ul><li>Audio Video</li><li>Cabling</li><li>Communication</li><li>Electronic Security</li><li>Project Consulting</li></ul>
  </div>

  <div class="abs" style="left:587px;top:3742px;width:40px;height:40px;border-radius:50%;background:#1c4fa6;border:2px solid #7fc4ff;display:flex;align-items:center;justify-content:center">
    <svg width="14" height="14" viewBox="0 0 14 14"><path d="M7,12 L7,2 M3,6 L7,2 L11,6" stroke="#fff" stroke-width="1.6" fill="none"/></svg>
  </div>
  <div class="abs" style="left:1155px;top:3780px;width:30px;height:30px;border-radius:50%;background:#fff;display:flex;align-items:center;justify-content:center">
    <svg width="12" height="12" viewBox="0 0 12 12"><path d="M2,8 L6,4 L10,8" stroke="#1b3d8f" stroke-width="1.6" fill="none"/></svg>
  </div>
  <p class="abs legal" style="left:141px;top:3800px">©2024 Silver Heron Systems. All rights reserved.</p>
  <p class="abs legal" style="left:871px;top:3800px">Site Terms&nbsp;&nbsp;|&nbsp;&nbsp;Privacy Policy</p>

</div>
</body>
</html>
```